Label Design for Bra "Heron Lingerie" by Larkfield Apparel Company

The bra is packaged in a poly bag with a hanger. We require a label design for the brand name "Heron Lingerie" by Larkfield Apparel Company. The main label will be attached by a string on the bra. The size of that label will 25cm in length and 10cm wide. This is the first label the customer see's when she picks up the garment/bra. Therefore, we require an eye catching design for that. This classic full shape bra with smooth moulded double layered cups fit beautifully under t-shirts and fitted garments. The larkfield apparel company logo has been included and we would like it to feature in the label. A sample labels are also given.
Target Market(s)
Laddies 18 - 45
Industry/Entity Type
Clothing
Look and feel
Each slider illustrates characteristics of the customer's brand and the style your logo design should communicate.

```html
<!DOCTYPE html>
<html lang="en">
<head>
<meta charset="utf-8">
<title>Heron Lingerie – Hang Label</title>
<link rel="stylesheet" href="https://fonts.googleapis.com/css2?family=Fredoka:wght@500&display=swap">
<style>
  :root {
    --paper: #ffffff;
    --label-brown: #331f16;
    --backdrop-shade: #1e1d1a;
    --title-white: #ffffff;
    --mark-grey: #c4c5c4;
  }
  html, body {
    margin: 0;
    padding: 0;
    width: 1200px;
    height: 2835px;
    overflow: hidden;
    background: var(--paper);
  }
  .label {
    position: relative;
    width: 1200px;
    height: 2835px;
    background: var(--paper);
  }
  .label-panel {
    position: absolute;
    left: 55px;
    top: 55px;
    width: 1093px;
    height: 2733px;
    background: var(--label-brown);
    overflow: hidden;
  }
  .backdrop-shape {
    position: absolute;
    left: 0;
    top: 220px;
    width: 790px;
    height: 1925px;
    background: var(--backdrop-shade);
    border-radius: 0 420px 420px 0;
  }
  .brand-title {
    position: absolute;
    left: 528px;
    top: 548px;
    margin: 0;
    writing-mode: vertical-rl;
    font-family: "Fredoka", sans-serif;
    font-weight: 500;
    font-size: 184px;
    line-height: 1;
    letter-spacing: 16px;
    color: var(--title-white);
    text-transform: lowercase;
    white-space: nowrap;
  }
  .maker {
    position: absolute;
    left: 55px;
    width: 1093px;
    top: 2236px;
    display: flex;
    flex-direction: column;
    align-items: center;
  }
  .maker-square {
    width: 190px;
    height: 190px;
    border-radius: 16px;
    background: var(--mark-grey);
    margin-bottom: 22px;
  }
  .maker-name {
    margin: 0;
    font-family: "Fredoka", sans-serif;
    font-weight: 500;
    color: var(--mark-grey);
    text-align: center;
    line-height: 1;
  }
  .maker-name .line-main {
    display: block;
    font-size: 116px;
  }
  .maker-name .line-sub {
    display: block;
    font-size: 52px;
    margin-top: 6px;
    letter-spacing: 1px;
  }
</style>
</head>
<body>
  <main class="label">
    <div class="label-panel">
      <div class="backdrop-shape" role="img" aria-label="Large dark brand decoration behind the title"></div>
    </div>
    <h1 class="brand-title">heron lingerie</h1>
    <footer class="maker">
      <div class="maker-square" aria-hidden="true"></div>
      <p class="maker-name">
        <span class="line-main">larkfield</span>
        <span class="line-sub">apparel company</span>
      </p>
    </footer>
  </main>
</body>
</html>
```